Professional Modern Website Design

We are a premium IT services provider to the financial industry based in London. Our company is called Veltra our current holding page is www.veltra-example.co.uk. We require a new website to match our new corporate identity. This project is for the design phase only. Development will be handled in-house. I have attached examples of wire frames we have developed (although open to suggestions for improvement) Our brand document that should demonstrate current brand, inc how we communicate to potential clients and finally mostly completed web-content.
We are looking for designers that can create something that sets us apart from our competitors.
Target Market(s)
IT Decision makers in Finance companies such as; hedge funds, private investment banks etc
Industry/Entity Type
Financial
Number of Pages Required
5+ page
Requirements
Must have
- hexagon elements in the design, unique design.
Nice to have
- Blog and social media feeds
Should not have
- Should not resemble a downloaded template

```html
<!DOCTYPE html>
<html lang="en">
<head>
<meta charset="utf-8">
<title>Veltra – Systems Integration for Finance</title>
<link href="https://fonts.googleapis.com/css2?family=Jost:wght@400;500;600;700&family=Open+Sans:wght@400;600&display=swap" rel="stylesheet">
<style>
:root{
  --orange:#f26a1b;
  --orange-deep:#e4570f;
  --orange-light:#f7941d;
  --ink:#222222;
  --body:#555555;
  --muted:#8a8a8a;
  --paper:#ffffff;
  --page:#efefef;
  --header:#ececec;
  --dark:#1b1b1b;
  --dark-2:#262626;
  --field:#e9e9e9;
}
*{box-sizing:border-box;margin:0;padding:0}
html,body{width:1200px;height:2567px;overflow:hidden}
body{position:relative;background:var(--page);font-family:"Open Sans",Arial,sans-serif;color:var(--body)}
.abs{position:absolute}
.heading{font-family:"Jost","Century Gothic",sans-serif;text-transform:uppercase}

/* header */
.site-header{left:0;top:0;width:1200px;height:165px;background:linear-gradient(100deg,var(--header) 60%,#f5f5f5 80%,#e6e6e6)}
.brand{left:73px;top:30px;display:flex;flex-direction:column;align-items:flex-start;gap:10px}
.brand-mark{width:70px;height:70px;background:var(--orange)}
.brand-name{font-family:"Jost",sans-serif;font-weight:500;font-size:20px;letter-spacing:6px;color:#666}
.phone{top:56px;display:flex;align-items:center;gap:14px;font-family:"Jost",sans-serif;color:var(--ink)}
.phone svg{width:40px;height:46px}
.phone .label{font-size:13px;text-transform:uppercase;line-height:1.1}
.phone .num{font-size:20px;line-height:1.2}

/* nav */
.main-nav{left:0;top:165px;width:1200px;height:49px;background:linear-gradient(90deg,var(--orange-deep),var(--orange) 50%,var(--orange-light))}
.main-nav a{position:absolute;top:15px;color:#fff;text-decoration:none;font-family:"Jost",sans-serif;font-weight:600;font-size:16px;text-transform:uppercase}
.social{position:absolute;top:17px;left:1030px;display:flex;gap:12px}
.social span{width:15px;height:15px;border-radius:50%;background:#fff;display:block}

/* hero */
.hero{left:0;top:214px;width:1200px;height:652px;background:linear-gradient(180deg,#2a2a2a,#151515)}
.slide{left:75px;top:6px;width:1050px;height:475px;border:6px solid var(--paper);background:linear-gradient(90deg,#f4f4f4,#dcdcdc 55%,#cfcfcf);overflow:hidden}
.slide-photo{position:absolute;right:0;top:0;width:520px;height:463px}
.slide-copy{position:absolute;left:86px;top:110px;width:360px}
.slide-copy h1{font-family:"Jost",sans-serif;font-weight:700;font-size:25px;line-height:1.1;color:var(--ink);text-transform:uppercase}
.slide-copy p{margin-top:20px;font-size:14.5px;line-height:1.6;color:#333}
.btn{display:inline-block;margin-top:20px;background:var(--orange);color:#fff;font-family:"Jost",sans-serif;font-size:14px;text-transform:uppercase;padding:10px 20px}
.arrow{top:214px;width:82px;height:48px;background:#3a3a3a}
.arrow svg{position:absolute;top:14px;width:20px;height:20px}
.intro{left:0;top:520px;width:1200px;text-align:center;color:#fff}
.intro h2{font-family:"Jost",sans-serif;font-weight:700;font-size:26px}
.intro p{margin:18px auto 0;width:780px;font-family:"Jost",sans-serif;font-size:17px;line-height:1.5;text-transform:uppercase}

/* audience cards */
.audience{left:0;top:866px;width:1200px;height:1134px;background:var(--page)}
.card{position:absolute;width:560px;height:500px}
.card .shape{position:absolute;left:79px;top:75px;width:470px;height:460px;filter:drop-shadow(0 2px 3px rgba(0,0,0,.12))}
.card .portrait{position:absolute;left:0;top:52px;width:207px;height:240px}
.card h3{position:absolute;left:235px;top:164px;width:265px;font-family:"Jost",sans-serif;font-weight:700;font-size:16px;line-height:1.25;color:var(--ink);text-transform:uppercase}
.card p{position:absolute;left:235px;top:212px;width:262px;font-size:13.2px;line-height:1.62;color:var(--body)}

/* footer */
.site-footer{left:0;top:2000px;width:1200px;height:567px;background:linear-gradient(180deg,var(--dark-2),var(--dark));border-top:4px solid var(--orange);color:#fff}
.footer-mark{left:575px;top:4px;width:50px;height:50px}
.footer-title{left:0;top:62px;width:1200px;text-align:center;font-family:"Jost",sans-serif;font-weight:700;font-size:23px}
.footer-rule{left:578px;top:100px;width:44px;height:3px;background:var(--orange)}
.office h4,.col h4{font-family:"Jost",sans-serif;font-weight:600;font-size:15px;text-transform:uppercase}
.office .addr,.office .contact{position:absolute;top:40px;font-family:"Jost",sans-serif;font-size:12.5px;line-height:1.5;text-transform:uppercase;color:#ccc;display:flex;gap:10px}
.office .contact b{color:var(--orange);font-weight:500}
.office svg{width:12px;height:16px;flex:none;margin-top:2px}
.footer-divider{left:73px;top:218px;width:1052px;height:1px;background:#3c3c3c}
.col .item{margin-top:24px;font-family:"Jost",sans-serif;text-transform:uppercase}
.col .date{font-size:11px;color:#777}
.col .title{font-size:13px;line-height:1.45;color:#ddd;margin-top:4px}
.field{position:absolute;background:var(--field);color:#888;font-size:11px;padding:8px 10px;text-transform:uppercase}
.submit{left:614px;top:505px;width:105px;height:32px;background:var(--orange);color:#fff;font-family:"Jost",sans-serif;font-weight:600;font-size:13px;text-align:center;line-height:32px}
.copyright{left:73px;top:515px;font-family:"Jost",sans-serif;font-size:11.5px;color:#aaa;text-transform:uppercase}
</style>
</head>
<body>

<header class="site-header abs">
  <div class="brand abs"><span class="brand-mark"></span><span class="brand-name">VELTRA</span></div>
  <div class="phone abs" style="left:672px">
    <svg viewBox="0 0 40 46"><polygon points="20,1 39,12 39,34 20,45 1,34 1,12" fill="none" stroke="#bbb" stroke-width="1.5"/><path d="M15 15c1-1 3-1 3 1l1 3c0 1-1 2-2 2 1 3 3 5 6 6 0-1 1-2 2-2l3 1c2 0 2 2 1 3-1 2-3 3-6 2-5-2-8-5-10-10-1-3 0-5 2-6z" fill="#888"/></svg>
    <div><div class="label">London</div><div class="num">+44 20 7946 0182</div></div>
  </div>
  <div class="phone abs" style="left:928px">
    <svg viewBox="0 0 40 46"><polygon points="20,1 39,12 39,34 20,45 1,34 1,12" fill="none" stroke="#bbb" stroke-width="1.5"/><path d="M15 15c1-1 3-1 3 1l1 3c0 1-1 2-2 2 1 3 3 5 6 6 0-1 1-2 2-2l3 1c2 0 2 2 1 3-1 2-3 3-6 2-5-2-8-5-10-10-1-3 0-5 2-6z" fill="#888"/></svg>
    <div><div class="label">Essex</div><div class="num">+44 20 7946 0183</div></div>
  </div>
</header>

<nav class="main-nav abs">
  <a href="#" style="left:107px">About</a>
  <a href="#" style="left:216px">Services</a>
  <a href="#" style="left:349px">Partners</a>
  <a href="#" style="left:481px">Clients</a>
  <a href="#" style="left:599px">Contact</a>
  <div class="social" aria-label="Social links"><span></span><span></span><span></span><span></span></div>
</nav>

<section class="hero abs">
  <div class="slide abs">
    <svg class="slide-photo" viewBox="0 0 520 463" role="img" aria-label="Black and white photo of a smiling businesswoman holding a tablet">
      <defs><linearGradient id="heroPhoto" x1="0" y1="0" x2="1" y2="1"><stop offset="0" stop-color="#e8e8e8"/><stop offset="0.6" stop-color="#b9b9b9"/><stop offset="1" stop-color="#7d7d7d"/></linearGradient></defs>
      <polygon points="70,0 520,0 520,463 70,463 0,232" fill="url(#heroPhoto)"/>
    </svg>
    <div class="slide-copy">
      <h1>You need integration.<br>We’re always there with you.</h1>
      <p>Veltra is one of the leading systems integrators to the world’s finance sector. We are an extension of your business and our services portfolio has been built so you always have access to a complete partner.</p>
      <span class="btn">About us</span>
    </div>
  </div>
  <div class="arrow abs" style="left:0;clip-path:polygon(0 0,85% 0,100% 50%,85% 100%,0 100%)"><svg viewBox="0 0 20 20" style="left:28px"><path d="M13 3 6 10l7 7" fill="none" stroke="#fff" stroke-width="2.5"/></svg></div>
  <div class="arrow abs" style="left:1118px;clip-path:polygon(15% 0,100% 0,100% 100%,15% 100%,0 50%)"><svg viewBox="0 0 20 20" style="left:34px"><path d="M7 3l7 7-7 7" fill="none" stroke="#fff" stroke-width="2.5"/></svg></div>
  <div class="intro abs">
    <h2>WHO ARE YOU?</h2>
    <p>If you’re part of a financial organisation, we have the power to help everyone work more efficiently, productively and profitably.</p>
  </div>
</section>

<section class="audience abs">
  <svg width="0" height="0" style="position:absolute">
    <defs>
      <linearGradient id="portraitFill" x1="0" y1="0" x2="1" y2="1"><stop offset="0" stop-color="#d9d4cf"/><stop offset="1" stop-color="#7b8591"/></linearGradient>
    </defs>
  </svg>

  <article class="card" style="left:71px;top:0">
    <svg class="shape" viewBox="0 0 470 460"><polygon points="235,0 470,115 470,345 235,460 0,345 0,115" fill="#fff"/></svg>
    <svg class="portrait" viewBox="0 0 207 240" role="img" aria-label="Portrait photo of a senior hedge fund manager in a suit">
      <polygon points="103,3 204,60 204,180 103,237 3,180 3,60" fill="none" stroke="var(--orange)" stroke-width="6"/>
      <polygon points="108,20 196,70 196,175 108,225 20,175 20,70" fill="url(#portraitFill)" stroke="var(--orange-light)" stroke-width="2"/>
    </svg>
    <h3>Senior hedge fund manager/CEO</h3>
    <p>You need to develop and implement strategies for business growth, while ensuring profitability. You’re aware your biggest asset is your staff and a happy workforce is a productive one. Security is a key concern in a changing always-on world and you need to be compliant, but you don’t want to over-spend. Veltra can help you find the best solutions to help your business grow at the speed you want it to.</p>
  </article>

  <article class="card" style="left:612px;top:0">
    <svg class="shape" viewBox="0 0 470 460"><polygon points="235,0 470,115 470,345 235,460 0,345 0,115" fill="#fff"/></svg>
    <svg class="portrait" viewBox="0 0 207 240" role="img" aria-label="Portrait photo of a smiling CFO with glasses">
      <polygon points="103,3 204,60 204,180 103,237 3,180 3,60" fill="none" stroke="var(--orange)" stroke-width="6"/>
      <polygon points="108,20 196,70 196,175 108,225 20,175 20,70" fill="url(#portraitFill)" stroke="var(--orange-light)" stroke-width="2"/>
    </svg>
    <h3>CFO</h3>
    <p>Your key responsibility is to obtain the maximum ROI from products and services. You understand investment opportunities, providing they return higher efficiencies and revenues. You are concerned more with long-term spending versus short-term and how you can get the most value out of a proposition. Veltra can advise how to boost ROI by streamlining your business to maximise return.</p>
  </article>

  <article class="card" style="left:71px;top:503px">
    <svg class="shape" viewBox="0 0 470 460"><polygon points="235,0 470,115 470,345 235,460 0,345 0,115" fill="#fff"/></svg>
    <svg class="portrait" viewBox="0 0 207 240" role="img" aria-label="Portrait photo of an IT manager in an office">
      <polygon points="103,3 204,60 204,180 103,237 3,180 3,60" fill="none" stroke="var(--orange)" stroke-width="6"/>
      <polygon points="108,20 196,70 196,175 108,225 20,175 20,70" fill="url(#portraitFill)" stroke="var(--orange-light)" stroke-width="2"/>
    </svg>
    <h3>IT Manager/CTO</h3>
    <p>Integration with partners and services is your key concern. You want to make sure any IT system you implement will work with the whole infrastructure of your company. You don’t want your team to waste valuable time dealing with things that don’t matter. Veltra provides the whole picture to ensure your company is ready for the next generation of IT.</p>
  </article>

  <article class="card" style="left:612px;top:503px">
    <svg class="shape" viewBox="0 0 470 460"><polygon points="235,0 470,115 470,345 235,460 0,345 0,115" fill="#fff"/></svg>
    <svg class="portrait" viewBox="0 0 207 240" role="img" aria-label="Group photo of office employees">
      <polygon points="103,3 204,60 204,180 103,237 3,180 3,60" fill="none" stroke="var(--orange)" stroke-width="6"/>
      <polygon points="108,20 196,70 196,175 108,225 20,175 20,70" fill="url(#portraitFill)" stroke="var(--orange-light)" stroke-width="2"/>
    </svg>
    <h3>Employees</h3>
    <p>You’re working hard, but not getting anywhere fast. You want the tools to make your job easier so you can spend more time thinking about what you’re doing rather than how you’re doing it. You shouldn’t have to think about the technology you’re using, because it should just work. Veltra can help you get back on track everyday.</p>
  </article>
</section>

<footer class="site-footer abs">
  <svg class="footer-mark abs" viewBox="0 0 50 50" aria-hidden="true"><rect x="5" y="5" width="40" height="40" fill="var(--orange)"/></svg>
  <div class="footer-title abs">GET IN TOUCH</div>
  <div class="footer-rule abs"></div>

  <div class="office abs" style="left:73px;top:132px;width:500px">
    <h4>London office</h4>
    <div class="addr" style="left:0"><svg viewBox="0 0 12 16"><path d="M6 0a6 6 0 0 0-6 6c0 4 6 10 6 10s6-6 6-10a6 6 0 0 0-6-6zm0 8a2 2 0 1 1 0-4 2 2 0 0 1 0 4z" fill="#777"/></svg><span>18 Harlow Street,<br>Mayfair, London W1A 2ZX</span></div>
    <div class="contact" style="left:270px"><svg viewBox="0 0 12 16"><path d="M2 2c1-1 2 0 2 1l1 3-1 1c1 2 2 3 3 4l1-1 3 1c1 0 1 2 0 3-2 2-5 1-8-3S0 4 2 2z" fill="#777"/></svg><span><b>T:</b> +44 20 7946 0182<br><b>E:</b> info@veltra-example.co.uk</span></div>
  </div>
  <div class="office abs" style="left:640px;top:132px;width:500px">
    <h4>Essex office</h4>
    <div class="addr" style="left:0"><svg viewBox="0 0 12 16"><path d="M6 0a6 6 0 0 0-6 6c0 4 6 10 6 10s6-6 6-10a6 6 0 0 0-6-6zm0 8a2 2 0 1 1 0-4 2 2 0 0 1 0 4z" fill="#777"/></svg><span>7 Elmgate Works, Elm Avenue<br>Southend, Essex SS1 9ZZ</span></div>
    <div class="contact" style="left:275px"><svg viewBox="0 0 12 16"><path d="M2 2c1-1 2 0 2 1l1 3-1 1c1 2 2 3 3 4l1-1 3 1c1 0 1 2 0 3-2 2-5 1-8-3S0 4 2 2z" fill="#777"/></svg><span><b>T:</b> +44 20 7946 0183<br><b>E:</b> info@veltra-example.co.uk</span></div>
  </div>

  <div class="footer-divider abs"></div>

  <div class="col abs" style="left:73px;top:246px;width:240px">
    <h4>Recent news</h4>
    <div class="item"><div class="date">10 Mar 2015</div><div class="title">Mirum est notare quam littera gothi ca, quam nunc</div></div>
    <div class="item" style="margin-top:30px"><div class="date">10 Mar 2015</div><div class="title">Mirum est notare quam littera gothi ca, quam nunc</div></div>
  </div>
  <div class="col abs" style="left:342px;top:246px;width:240px">
    <h4>Recent blog</h4>
    <div class="item"><div class="date">10 Mar 2015 | 10 Comments</div><div class="title">Mirum est notare quam littera gothi ca, quam nunc</div></div>
    <div class="item" style="margin-top:30px"><div class="date">10 Mar 2015 | 10 Comments</div><div class="title">Mirum est notare quam littera gothi ca, quam nunc</div></div>
  </div>
  <div class="col abs" style="left:614px;top:246px;width:511px">
    <h4>Contact Veltra</h4>
  </div>
  <div class="field" style="left:614px;top:276px;width:250px;height:32px">Name</div>
  <div class="field" style="left:875px;top:276px;width:250px;height:32px">Email</div>
  <div class="field" style="left:614px;top:318px;width:511px;height:176px">Message</div>
  <div class="submit abs">SUBMIT</div>

  <div class="copyright abs">© 2015 Veltra Limited. All rights reserved.</div>
</footer>

</body>
</html>
```